Personal Training

Personal Fitness Trainer
Sports Nutritionist
Individual and Group rates available
Certifications
Global Wellness Coaches Federation
Worldwide Athletic Study Council

Industry/Entity Type

Fitness

Contact Information for Business Card

Dorinda Valcourt
555-284-7160
dvalcourt4@brimfeld.com

```html
<!DOCTYPE html>
<html lang="en">
<head>
<meta charset="utf-8">
<title>Dorinda Valcourt – Personal Training Business Card</title>
<link rel="stylesheet" href="https://fonts.googleapis.com/css2?family=Alfa+Slab+One&family=Rokkitt:wght@400&family=Arimo:wght@400&display=swap">
<style>
  :root {
    --card-bg: #171717;
    --teal: #11a39e;
    --teal-band: #00a49f;
    --teal-rule: #2c8a86;
    --white: #ffffff;
  }
  html, body {
    margin: 0;
    padding: 0;
    width: 1200px;
    height: 702px;
    overflow: hidden;
    background: var(--card-bg);
  }
  .card {
    position: relative;
    width: 1200px;
    height: 702px;
    background: var(--card-bg);
    overflow: hidden;
  }
  .figure-art {
    position: absolute;
    left: 61px;
    top: 205px;
    width: 334px;
    height: 267px;
    border-radius: 50% / 45%;
    background: radial-gradient(ellipse at 50% 50%, var(--teal) 0%, rgba(17,163,158,0.75) 45%, rgba(17,163,158,0) 72%);
  }
  .divider {
    position: absolute;
    left: 447px;
    top: 160px;
    width: 2px;
    height: 358px;
    background: var(--teal-rule);
  }
  .info {
    position: absolute;
    left: 470px;
    width: 686px;
    text-align: center;
    margin: 0;
  }
  .name {
    top: 52px;
    font-family: "Alfa Slab One", serif;
    font-weight: 400;
    font-size: 54px;
    line-height: 1;
    letter-spacing: 1px;
    color: var(--white);
    text-transform: uppercase;
  }
  .roles {
    top: 153px;
    font-family: "Rokkitt", serif;
    font-size: 40px;
    line-height: 49px;
    color: var(--teal);
    text-transform: uppercase;
  }
  .cert-heading {
    top: 305px;
    font-family: "Rokkitt", serif;
    font-size: 31px;
    line-height: 1.2;
    color: var(--teal);
  }
  .cert-list {
    top: 343px;
    font-family: "Rokkitt", serif;
    font-size: 31px;
    line-height: 39px;
    color: var(--white);
    list-style: none;
    padding: 0;
  }
  .rates {
    top: 490px;
    font-family: "Rokkitt", serif;
    font-size: 31px;
    line-height: 1.2;
    color: var(--teal);
  }
  .contact-band {
    position: absolute;
    left: 0;
    top: 587px;
    width: 1200px;
    height: 70px;
    background: var(--teal-band);
    font-family: "Arimo", sans-serif;
    font-size: 32px;
    color: var(--white);
  }
  .contact-band span {
    position: absolute;
    top: 50%;
    transform: translate(-50%, -50%);
    white-space: nowrap;
  }
  .phone { left: 227px; }
  .email { left: 815px; }
</style>
</head>
<body>
  <div class="card">
    <div class="figure-art" role="img" aria-label="Silhouette of a woman lifting a dumbbell inside a swoosh ring"></div>
    <div class="divider"></div>

    <h1 class="info name">Dorinda Valcourt</h1>
    <p class="info roles">Personal Fitness Trainer<br>Sports Nutritionist</p>
    <p class="info cert-heading">Certifications</p>
    <ul class="info cert-list">
      <li>Global Wellness Coaches Federation</li>
      <li>Worldwide Athletic Study Council</li>
    </ul>
    <p class="info rates">Individual and Group Rates Available</p>

    <div class="contact-band">
      <span class="phone">555-284-7160</span>
      <span class="email">dvalcourt4@brimfeld.com</span>
    </div>
  </div>
</body>
</html>
```